Brightwire Hollow Business cards

one side I would like my logo (uploaded) and the other side I want my details. I'm an electrician in sydney. The logo side I'm happy with just a white background and our logo in the middle.

Details for other side
24/7 Sydney Electrician
Marcus Pell
0431 587 219
marcus@brightwirehollow.com.au
brightwirehollow.com.au
icons for facebook, instagram, linked in

Industry/Entity Type

electrician

Contact Information for Business Card

company info

```html
<!DOCTYPE html>
<html lang="en">
<head>
<meta charset="utf-8">
<title>Brightwire Hollow – Business Card</title>
<link rel="stylesheet" href="https://fonts.googleapis.com/css2?family=Lexend+Exa:wght@400;500;700&display=swap">
<style>
  :root {
    --card-red: #fe1a04;
    --ink-white: #ffffff;
    --ink-black: #111111;
    --paper: #ffffff;
    --pattern-pink: rgba(255, 190, 180, 0.55);
    --pattern-soft: rgba(250, 120, 105, 0.28);
  }
  * { box-sizing: border-box; margin: 0; padding: 0; }
  html, body {
    width: 1200px;
    height: 804px;
    overflow: hidden;
    background: var(--paper);
  }
  .canvas {
    position: relative;
    width: 1200px;
    height: 804px;
    background: var(--paper);
    font-family: "Lexend Exa", sans-serif;
    color: var(--ink-white);
  }
  .margin-texture {
    position: absolute;
    inset: 0;
    background:
      radial-gradient(ellipse 420px 60px at 700px 10px, var(--pattern-soft), transparent 75%),
      radial-gradient(ellipse 40px 380px at 10px 470px, var(--pattern-soft), transparent 75%),
      radial-gradient(ellipse 60px 300px at 1190px 560px, var(--pattern-soft), transparent 75%);
  }
  .card {
    position: absolute;
    left: 39px;
    top: 39px;
    width: 1122px;
    height: 726px;
    background: var(--card-red);
    overflow: hidden;
  }
  .card-texture {
    position: absolute;
    inset: 0;
    background:
      radial-gradient(ellipse 560px 520px at 1122px 0px, var(--pattern-pink), rgba(255,170,160,0.25) 45%, transparent 80%),
      radial-gradient(ellipse 260px 420px at 1122px 420px, rgba(255,160,150,0.22), transparent 80%);
  }
  .brand-name {
    position: absolute;
    left: 117px;
    top: 118px;
    font-weight: 700;
    font-size: 40px;
    line-height: 1.05;
    letter-spacing: 0.06em;
    text-transform: uppercase;
    color: var(--ink-white);
  }
  .person-name {
    position: absolute;
    left: 115px;
    top: 270px;
    font-weight: 700;
    font-size: 44px;
    letter-spacing: 0.01em;
    line-height: 1;
  }
  .contact-list {
    position: absolute;
    left: 121px;
    top: 334px;
    list-style: none;
  }
  .contact-item {
    display: flex;
    align-items: center;
    height: 46px;
    font-weight: 500;
    line-height: 1;
  }
  .contact-item .icon {
    width: 24px;
    height: 24px;
    margin-right: 20px;
    flex: none;
  }
  .contact-phone { font-size: 36px; height: 50px; }
  .contact-email, .contact-web { font-size: 32px; }
  .social-row {
    position: absolute;
    left: 122px;
    top: 475px;
    display: flex;
    gap: 14px;
  }
  .social-dot {
    width: 26px;
    height: 26px;
    border-radius: 50%;
    background: var(--ink-black);
  }
  .tagline {
    position: absolute;
    left: 0;
    width: 100%;
    top: 586px;
    text-align: center;
    font-weight: 500;
    font-size: 40px;
    letter-spacing: 0.05em;
    line-height: 1;
  }
</style>
</head>
<body>
  <main class="canvas">
    <div class="margin-texture" role="img" aria-label="Faint pale red plug pattern around the card edges"></div>
    <section class="card">
      <div class="card-texture" role="img" aria-label="Repeating pale plug pattern fading across the upper right of the card"></div>

      <div class="brand-name">Brightwire<br>Hollow</div>

      <h1 class="person-name">Marcus Pell</h1>

      <ul class="contact-list">
        <li class="contact-item contact-phone">
          <svg class="icon" viewBox="0 0 24 24" aria-hidden="true">
            <path fill="#111" d="M6.6 10.8a15.1 15.1 0 0 0 6.6 6.6l2.2-2.2c.3-.3.7-.4 1-.2 1.1.4 2.3.6 3.6.6.6 0 1 .4 1 1V20c0 .6-.4 1-1 1A17 17 0 0 1 3 4c0-.6.4-1 1-1h3.5c.6 0 1 .4 1 1 0 1.3.2 2.5.6 3.6.1.3 0 .7-.2 1z"/>
          </svg>
          <span>0431 587 219</span>
        </li>
        <li class="contact-item contact-email">
          <svg class="icon" viewBox="0 0 24 24" aria-hidden="true">
            <rect x="2" y="6" width="20" height="13" fill="#111"/>
            <path d="M2.5 6.5 12 13.5l9.5-7M2.5 18.5l7-6M21.5 18.5l-7-6" stroke="#fe1a04" stroke-width="1.3" fill="none"/>
          </svg>
          <span>marcus@brightwirehollow.com.au</span>
        </li>
        <li class="contact-item contact-web">
          <svg class="icon" viewBox="0 0 24 24" aria-hidden="true">
            <circle cx="12" cy="12" r="9" fill="#111"/>
            <g stroke="#fe1a04" stroke-width="1.2" fill="none">
              <ellipse cx="12" cy="12" rx="4" ry="9"/>
              <path d="M12 3v18M3 12h18M4.5 7.5h15M4.5 16.5h15"/>
            </g>
          </svg>
          <span>brightwirehollow.com.au</span>
        </li>
      </ul>

      <div class="social-row" aria-label="Social media links">
        <span class="social-dot"></span>
        <span class="social-dot"></span>
      </div>

      <p class="tagline">24/7 SYDNEY ELECTRICIAN</p>
    </section>
  </main>
</body>
</html>
```